Paleo Diet Book Cover Design

I need a cover designed for my book Stone Frame that will be sold on Rivora Pageleaf and other sites. So the front, side and back will need to be designed. I have attached part of the book here so feel free to skim through the content and give it a quick read to get a feel for what the book is about. Stone Frame is about eating the diet of the caveman (paleolithic era-paleo) and a 12 week workout plan with a grocery shopping list and meal plans. It is for men and women ages 18+ who are interested in health and fitness and becoming healthier overall.
The graphics should be secondary, and it should add to the text, not distract from it. This is even more important because the size of the cover displayed on Rivora/Pageleaf, when your book is first seen by a potential buyer, is so tiny. It's barely an inch high, and even smaller in width.
So the words have to be big, bold, benefit-rich and easy to read. That also means, don't mess with the fancy fonts. Clean, clear, crisp font is best. And, did I say BIG already?
Contrast the colors of the text and background, so its even easier to read. That means, dark text on light background or visa versa. Colors like darker reds, blues / teals and oranges.
Please read this: http://www.bookvantrel.com/8-cover-design-secrets-publishers-use-to-manipulate-readers-into-buying-books/
The cover has to be bold and easy to read, it has to stick out, it has to draw the attention of your readers so that they zero in on my book, out of all the other books on the page. (Much like they would when viewing a classified ads site/page.)
The Title of the Book is Stone Frame, and the subtitle is "Transform Your Body For Life in 12 Weeks With Proven Workouts and Paleo Diet Based Nutrition" Perhaps “Transform Your Body For Life in 12 Weeks” could also be in a large font similar to the title with the rest of the subtitle following afterwards. You can try having the title be the smaller font with the subtitle being the larger font as well.
Then the authors name "Colin Marsh” incorporated into the design.
I am not sure what to use as the background type of design for the front of the book so feel free to be creative with that.
The size needs to be 1563 pixels on the shortest side and 2500 pixels on the longest side just for the front of the cover.

```html
<!DOCTYPE html>
<html lang="en">
<head>
<meta charset="utf-8">
<title>Stone Frame – Front Cover</title>
<link rel="stylesheet" href="https://fonts.googleapis.com/css2?family=Dosis:wght@500;600&family=Oswald:wght@500;600&family=Open+Sans:wght@400&display=swap">
<style>
  :root {
    --paper: #ffffff;
    --frame: #3a3a3a;
    --title-top: #f8bd2a;
    --title-bottom: #e5850c;
    --deep-red: #8e1a1a;
    --band-red: #a3111a;
    --burst: #f2a81c;
    --burst-edge: #f9d27a;
    --figure-light: #f7b733;
    --figure-dark: #e38a10;
    --footer-orange: #efa00e;
    --white: #ffffff;
  }
  html, body {
    margin: 0;
    padding: 0;
    width: 937px;
    height: 1200px;
    overflow: hidden;
    background: var(--paper);
  }
  .cover {
    position: relative;
    width: 937px;
    height: 1200px;
    background: var(--paper);
    box-sizing: border-box;
    border: 2px solid var(--frame);
    overflow: hidden;
  }
  .cover-title {
    position: absolute;
    left: 0;
    top: 0;
    width: 933px;
    height: 280px;
  }
  .cover-title text {
    font-family: "Dosis", sans-serif;
    font-weight: 500;
    font-size: 310px;
  }
  .hero-figure {
    position: absolute;
    left: 28px;
    top: 326px;
    width: 124px;
    height: 332px;
    border-radius: 56px 56px 18px 18px;
    background: linear-gradient(180deg, var(--figure-light), var(--figure-dark));
  }
  .promise {
    position: absolute;
    left: 165px;
    top: 330px;
    width: 430px;
    margin: 0;
    font-family: "Dosis", sans-serif;
    font-weight: 600;
    font-size: 84px;
    line-height: 122px;
    color: var(--deep-red);
    text-align: center;
    text-transform: uppercase;
  }
  .promise span { display: block; }
  .burst {
    position: absolute;
    left: 592px;
    top: 395px;
    width: 316px;
    height: 208px;
  }
  .burst text {
    font-family: "Oswald", sans-serif;
    font-weight: 600;
    fill: var(--white);
    text-anchor: middle;
  }
  .feature-band {
    position: absolute;
    left: 0;
    top: 738px;
    width: 100%;
    height: 174px;
    background: var(--band-red);
    color: var(--white);
    font-family: "Oswald", sans-serif;
    font-weight: 500;
    text-align: center;
    text-transform: uppercase;
  }
  .feature-band .line-one {
    position: absolute;
    left: 0; right: 0;
    top: 18px;
    font-size: 60px;
    line-height: 74px;
    letter-spacing: 1px;
  }
  .feature-band .line-two {
    position: absolute;
    left: 0; right: 0;
    top: 94px;
    font-size: 48px;
    line-height: 60px;
    letter-spacing: 1px;
  }
  .author-footer {
    position: absolute;
    left: 0;
    top: 912px;
    width: 100%;
    height: 288px;
    background: linear-gradient(180deg, var(--paper) 0%, #fbe2b0 22%, var(--footer-orange) 62%, var(--footer-orange) 100%);
  }
  .author-name {
    position: absolute;
    left: 0; right: 0;
    top: 166px;
    margin: 0;
    font-family: "Open Sans", sans-serif;
    font-weight: 400;
    font-size: 52px;
    line-height: 64px;
    color: var(--white);
    text-align: center;
  }
</style>
</head>
<body>
  <main class="cover">
    <svg class="cover-title" viewBox="0 0 933 280" aria-label="Stone Frame">
      <defs>
        <linearGradient id="titleFill" x1="0" y1="0" x2="0" y2="1">
          <stop offset="0.1" stop-color="var(--title-top)"/>
          <stop offset="0.95" stop-color="var(--title-bottom)"/>
        </linearGradient>
      </defs>
      <text x="24" y="256" textLength="885" lengthAdjust="spacingAndGlyphs" fill="url(#titleFill)">STONE FRAME</text>
    </svg>

    <div class="hero-figure" role="img" aria-label="Orange silhouette of a muscular athlete posing"></div>

    <h2 class="promise">
      <span>Transform</span>
      <span>Your Body</span>
      <span>For Life</span>
    </h2>

    <svg class="burst" viewBox="-160 -106 320 212" aria-label="In just 12 weeks">
      <polygon fill="var(--burst)" stroke="var(--burst-edge)" stroke-width="3"
        points="156,0 122.6,15.6 144.1,39.1 103.9,44.5 110.3,72.1 69.5,66.5 59.7,94.2 24.4,78.5 0,102 -24.4,78.5 -59.7,94.2 -69.5,66.5 -110.3,72.1 -103.9,44.5 -144.1,39.1 -122.6,15.6 -156,0 -122.6,-15.6 -144.1,-39.1 -103.9,-44.5 -110.3,-72.1 -69.5,-66.5 -59.7,-94.2 -24.4,-78.5 0,-102 24.4,-78.5 59.7,-94.2 69.5,-66.5 110.3,-72.1 103.9,-44.5 144.1,-39.1 122.6,-15.6"/>
      <text x="0" y="-6" font-size="48">IN JUST</text>
      <text x="0" y="44" font-size="44">12 WEEKS</text>
    </svg>

    <section class="feature-band">
      <div class="line-one">With Proven Workouts</div>
      <div class="line-two">Paleo Diet Based Nutrition</div>
    </section>

    <footer class="author-footer">
      <p class="author-name">Colin Marsh</p>
    </footer>
  </main>
</body>
</html>
```